Brochure and Flyer template, Aluminium Facade company
Verdantis Structural Concepts pty Ltd
We are looking for a cutting edge Brochure and Flyer template that we can change text and pictures for different marketing products and services we provide to different target markets and audiences. We like a mixture of A4 size but also like the A5 size so please feel free to be creative.
Construction
Corporate, Building Companies, Architects, Home owners.
We are needing the Brochure template to cater for multiple product pictures and descriptions in either A4 or A5 format (please be creative) and the flier template is more aimed to focus on 1 or 2 individual products.
1 of 2 files of Past project photos for your use if you like
Our Logo
Our Logo Different Format
Our Company Profile (old and out dated for reference only!)
2 of 2 files of Past project photos for your use if you like
Past Projects for information on our company
SOME of our standard Products FOR YOUR INFORMATION ONLY
Havenor opening roof System Photos to go with the operable section Please make sure the Havenor logo is used
Our Products and Services description
Havenor opening Roof information
More Havenor opening roof pics and data. May be of use

```html
<!DOCTYPE html>
<html lang="en">
<head>
<meta charset="utf-8">
<title>Verdantis Structural Concepts – Havenor Opening Roof Flyer</title>
<link rel="stylesheet" href="https://fonts.googleapis.com/css2?family=Open+Sans:wght@400;600;700&display=swap">
<style>
  :root{
    --stage:#e9e9e6;
    --paper:#ffffff;
    --green:#2f9a4b;
    --green-bright:#1fae4a;
    --green-dark:#2f4a3f;
    --slate:#3d5148;
    --ink:#3a3a3a;
    --muted:#6b6b6b;
    --sky-light:#eef1f3;
    --sky-mid:#c9d2d8;
    --timber:#b07a4a;
    --grass:#5f8a3a;
  }
  *{box-sizing:border-box;margin:0;padding:0}
  html,body{width:1200px;height:901px;overflow:hidden}
  body{background:var(--stage);font-family:"Open Sans",Arial,sans-serif;color:var(--ink);position:relative}

  .flyer{position:absolute;left:295px;top:20px;width:610px;height:861px;background:var(--paper);
    box-shadow:0 6px 22px rgba(0,0,0,.18);overflow:hidden}

  .hero{position:absolute;left:0;top:0;width:610px;height:205px;display:flex}
  .hero-grass{width:120px;height:100%;background:linear-gradient(160deg,#7aa24a,var(--grass) 60%,#3f6a2a)}
  .hero-roof{flex:1;height:100%;background:linear-gradient(170deg,var(--sky-light) 0%,#dfe4e8 45%,var(--sky-mid) 75%,var(--timber) 100%)}

  .intro{position:absolute;left:0;top:205px;width:610px;height:72px;
    background:linear-gradient(90deg,var(--slate),var(--green) 70%,var(--green-bright));
    padding:14px 34px;color:#fff;font-size:11.5px;line-height:1.5}

  .body{position:absolute;left:0;top:277px;width:610px;height:470px;padding:26px 34px 0}
  .lists{position:absolute;left:34px;top:26px;width:300px}
  .section-title{color:var(--green);font-weight:700;font-size:15px;letter-spacing:.06em;margin-bottom:8px}
  .lists ul{list-style:none;font-size:11.5px;line-height:1.75;color:var(--ink);margin-bottom:20px}
  .lists li{padding-left:14px;position:relative}
  .lists li::before{content:"";position:absolute;left:0;top:7px;width:6px;height:6px;background:var(--green);border-radius:50%}

  .gallery{position:absolute;right:34px;top:26px;width:236px;display:grid;
    grid-template-columns:1fr 1fr;gap:6px}
  .gallery .photo{height:92px}
  .gallery .wide{grid-column:span 2;height:122px}
  .photo-roof{background:linear-gradient(160deg,#f2f4f5,#c7cdd1 60%,#8c8f8a)}
  .photo-sky{background:linear-gradient(180deg,#9cc3e4,#dfe7ee 60%,#8a8f86)}
  .photo-garden{background:linear-gradient(180deg,#d9dcd6,#8fa36b 70%,#5b6f3f)}
  .photo-patio{background:linear-gradient(170deg,#eceae4,#c9b79a 55%,#7f6a52)}

  .footer{position:absolute;left:0;bottom:0;width:610px;height:112px;
    background:linear-gradient(90deg,var(--green-dark),var(--slate) 55%,var(--green) 100%);
    display:flex;align-items:center;justify-content:space-between;padding:0 34px;color:#fff}
  .contact{font-size:11.5px;line-height:1.7}
  .brand{display:flex;align-items:center;gap:10px}
  .brand-dot{width:26px;height:26px;border-radius:50%;background:#fff}
  .brand-name{font-size:22px;font-weight:700;letter-spacing:.08em;color:#fff}
</style>
</head>
<body>
  <article class="flyer">
    <header class="hero">
      <div class="hero-grass" role="img" aria-label="Garden lawn beside a patio"></div>
      <div class="hero-roof" role="img" aria-label="Looking up through open aluminium louvre roof blades to the sky"></div>
    </header>

    <p class="intro">The Havenor Opening Roof is an adjustable louvre system that lets you control sun, shade and airflow at the touch of a button, turning any outdoor space into a year round living area.</p>

    <section class="body">
      <div class="lists">
        <h2 class="section-title">FEATURES</h2>
        <ul class="features">
          <li>Opens for natural light and air</li>
          <li>Closes for full weather protection</li>
          <li>Louvres rotate up to 170 degrees</li>
          <li>Integrated gutter and drainage system</li>
          <li>Rain sensor closes roof automatically</li>
          <li>Powder coated marine grade aluminium</li>
          <li>Remote or wall switch control</li>
          <li>Simple to install and maintain</li>
        </ul>
        <h2 class="section-title">BENEFITS</h2>
        <ul class="benefits">
          <li>Enjoy your outdoor area in all seasons</li>
          <li>Reduce heat and glare inside your home</li>
          <li>Add value and style to your property</li>
          <li>Custom sizes to suit any space</li>
          <li>Low maintenance, long lasting finish</li>
          <li>Designed and built to Australian standards</li>
          <li>Choose from a wide range of colours</li>
        </ul>
      </div>

      <div class="gallery">
        <div class="photo wide photo-roof" role="img" aria-label="Opening roof louvres seen from below"></div>
        <div class="photo photo-sky" role="img" aria-label="Louvre roof partly open against blue sky"></div>
        <div class="photo photo-garden" role="img" aria-label="Pergola with opening roof over a garden"></div>
        <div class="photo wide photo-patio" role="img" aria-label="Covered patio with louvre roof and outdoor furniture"></div>
      </div>
    </section>

    <footer class="footer">
      <address class="contact" style="font-style:normal">
        Address, Location, ABC<br>
        Phone: 123 456 4444<br>
        Email: name@website.com
      </address>
      <div class="brand">
        <span class="brand-dot"></span>
        <span class="brand-name">VERDANTIS</span>
      </div>
    </footer>
  </article>
</body>
</html>
```